Custom Signage and graphics need a vehicle design on 2019 Vorn Duo Hull Pickup Truck. 6'6...

we need a concept for our pick up truck. we specialize in custom exterior and interior signage and graphics. Not a full wrap. Partial wrap or decals.

Target Market(s)

Marketing Agencies, Developers, Builders.

Colors

Designer to choose colors to be used in the design.

Requirements
Must have
• logo
• website - zelvoa.ca
• social media (facebook,instagram, twitter)
• phone # - 319-555-0176

```html
<!DOCTYPE html>
<html lang="en">
<head>
<meta charset="utf-8">
<title>Zelvoa – Vorn Duo Hull Partial Wrap Layout</title>
<link rel="stylesheet" href="https://fonts.googleapis.com/css2?family=Montserrat:wght@700;800&display=swap">
<style>
  :root {
    --navy: #0f4a8a;
    --blue: #1b6fb6;
    --sky: #4b97d3;
    --ink: #0d3f78;
    --white: #ffffff;
    --paper: #ffffff;
    --edge: #d6dbe1;
    --label: #8a95a3;
  }
  * { margin: 0; padding: 0; box-sizing: border-box; }
  html, body { width: 1200px; height: 1200px; overflow: hidden; background: var(--paper); }
  .canvas { position: relative; width: 1200px; height: 1200px; font-family: "Montserrat", sans-serif; }

  .panel { position: absolute; background: var(--white); border: 2px solid var(--edge); border-radius: 14px; overflow: hidden; }
  .panel svg.bands { position: absolute; left: 0; top: 0; width: 100%; height: 100%; }

  .brand { position: absolute; display: flex; align-items: center; gap: 16px; }
  .brand-dot { border-radius: 50%; background: var(--navy); flex: none; }
  .brand-name { font-family: "Montserrat", sans-serif; font-weight: 800; color: var(--navy); line-height: 1; white-space: nowrap; }

  .phone { position: absolute; font-weight: 800; color: var(--ink); letter-spacing: 1px; white-space: nowrap; }
  .web { position: absolute; font-weight: 700; letter-spacing: 3px; white-space: nowrap; }
  .social { position: absolute; display: flex; gap: 6px; }
  .social span { display: block; border-radius: 50%; background: var(--navy); }
  .social.light span { background: var(--white); }

  /* side */
  .side { left: 50px; top: 150px; width: 1100px; height: 340px; }
  .side .brand { left: 60px; top: 78px; }
  .side .brand-dot { width: 96px; height: 96px; }
  .side .brand-name { font-size: 84px; }
  .side .web { left: 120px; top: 252px; font-size: 26px; color: var(--white); }
  .side .phone { right: 70px; top: 70px; font-size: 46px; }
  .side .social { right: 72px; top: 132px; }
  .side .social span { width: 22px; height: 22px; }

  /* tailgate */
  .tailgate { left: 60px; top: 640px; width: 500px; height: 220px; }
  .tailgate .phone { left: 24px; top: 18px; font-size: 22px; }
  .tailgate .web { right: 22px; top: 22px; font-size: 15px; letter-spacing: 2px; color: var(--ink); }
  .tailgate .brand { left: 60px; top: 72px; gap: 12px; }
  .tailgate .brand-dot { width: 66px; height: 66px; }
  .tailgate .brand-name { font-size: 56px; }
  .tailgate .social { right: 26px; top: 178px; }
  .tailgate .social span { width: 12px; height: 12px; }

  /* hood */
  .hood { left: 640px; top: 640px; width: 500px; height: 220px; }
  .hood .brand { left: 40px; top: 38px; gap: 12px; }
  .hood .brand-dot { width: 40px; height: 40px; }
  .hood .brand-name { font-size: 36px; }
  .grille-frame { position: absolute; left: 90px; top: 112px; width: 320px; height: 86px; border: 18px solid var(--navy); border-radius: 20px; }
  .grille-frame::after { content: ""; position: absolute; left: 50%; top: -18px; width: 16px; height: 86px; margin-left: -8px; background: var(--navy); }

  .caption { position: absolute; font-family: "Montserrat", sans-serif; font-weight: 700; font-size: 14px; letter-spacing: 3px; color: var(--label); text-transform: uppercase; }
</style>
</head>
<body>
<main class="canvas">

  <p class="caption" style="left:52px; top:118px;">Vorn Duo Hull · Driver Side</p>
  <section class="panel side" aria-label="Side decal layout">
    <svg class="bands" viewBox="0 0 1100 340" preserveAspectRatio="none" aria-hidden="true">
      <polygon points="0,250 1100,150 1100,340 0,340" fill="var(--sky)"/>
      <polygon points="0,275 1100,185 1100,340 0,340" fill="var(--blue)"/>
      <polygon points="0,310 1100,230 1100,340 0,340" fill="var(--navy)"/>
    </svg>
    <div class="brand">
      <span class="brand-dot"></span>
      <span class="brand-name">ZELVOA</span>
    </div>
    <p class="web">www.zelvoa.ca</p>
    <p class="phone">319-555-0176</p>
    <div class="social" aria-label="Social media"><span></span><span></span><span></span></div>
  </section>

  <p class="caption" style="left:62px; top:608px;">Tailgate</p>
  <section class="panel tailgate" aria-label="Tailgate decal layout">
    <svg class="bands" viewBox="0 0 500 220" preserveAspectRatio="none" aria-hidden="true">
      <rect x="0" y="168" width="500" height="52" fill="var(--sky)"/>
      <rect x="0" y="176" width="500" height="44" fill="var(--blue)"/>
      <rect x="0" y="200" width="500" height="20" fill="var(--navy)"/>
    </svg>
    <p class="phone">319-555-0176</p>
    <p class="web">www.zelvoa.ca</p>
    <div class="brand">
      <span class="brand-dot"></span>
      <span class="brand-name">ZELVOA</span>
    </div>
    <div class="social light" aria-label="Social media"><span></span><span></span><span></span></div>
  </section>

  <p class="caption" style="left:642px; top:608px;">Hood &amp; Grille</p>
  <section class="panel hood" aria-label="Hood decal and grille surround layout">
    <div class="brand">
      <span class="brand-dot"></span>
      <span class="brand-name">ZELVOA</span>
    </div>
    <div class="grille-frame"></div>
  </section>

</main>
</body>
</html>
```